Infographic style Media Kit for local newspaper

We are a local newspaper group based in Australia. We seek to create a 3 page infographic stylized media kit as follows:

Format: Adobe Illustrator
Description: Small Business Media kit
Pages: 4
Size: A4 (210 x 297)
Content:
...Page 1: Intro page (not required to be designed at this stage)
...Page 2 : About Australian Community Newspapers;
...Page 3 : About our Local Newspaper (the Ridgeline Courier)
...Page 4 : Price List and contact information
Style: Serious, clean, modern, corporate, not too cartoonish
Colors: Try to tie in/relate the document colors to the colors of the newspaper mastheads which are blue and red (samples of logos provided for color checking)

As this will be reproduced simply on a color laser printer, we prefer a clean look with a white background.

I HAVE ATTACHED SOME EXAMPLES OF INFOGRAPHICS TO GET AN UNDERSTANDING OF STYLE

We have attached the 3 pages including all text to be used as a guideline. Feel free to layout each page differently as long as it conforms to a logical grouping.

```html
<!DOCTYPE html>
<html lang="en">
<head>
<meta charset="utf-8">
<title>Australian Community Newspapers – Media Kit</title>
<link rel="stylesheet" href="https://fonts.googleapis.com/css2?family=Bebas+Neue&family=Oswald:wght@300;400;500&family=Josefin+Sans:wght@400;600&family=Open+Sans:wdth,wght@75..100,300..800&display=swap">
<style>
:root{
  --paper:#f3f3f2;
  --ink:#141414;
  --blue:#1b95d3;
  --red:#a53a3a;
  --red-soft:#d48a8a;
  --grey:#6d6d6d;
  --mid-grey:#9a9a9a;
  --rule:#3a3a3a;
}
*{box-sizing:border-box;margin:0;padding:0}
html,body{width:848px;height:1200px;overflow:hidden;background:var(--paper)}
.kit{position:relative;width:848px;height:1200px;background:var(--paper);color:var(--ink);font-family:"Open Sans",sans-serif;font-stretch:87.5%}
.abs{position:absolute;white-space:nowrap}
.display{font-family:"Bebas Neue",sans-serif;line-height:.85;transform-origin:left top}

/* masthead */
.masthead-top{left:19px;top:14px;font-size:104px;color:var(--blue);transform:scaleX(1.3)}
.masthead-main{left:24px;top:95px;font-size:114px;transform:scaleX(.91)}
.bubble{left:603px;top:8px;width:216px;height:60px;border:1.5px solid var(--ink);border-radius:6px;background:#fff;font-size:12px;font-stretch:100%;line-height:1.35;padding:5px 9px;white-space:nowrap}
.bubble::after{content:"";position:absolute;left:36px;bottom:-9px;width:14px;height:14px;background:#fff;border-right:1.5px solid var(--ink);border-bottom:1.5px solid var(--ink);transform:skewX(35deg) rotate(45deg)}
.hatch{left:24px;width:800px;height:7px;background:repeating-linear-gradient(120deg,var(--ink) 0 2px,transparent 2px 6px)}
.rule{height:1.5px;background:var(--rule)}

/* readership */
.big-stat{font-family:"Oswald",sans-serif;font-weight:400;color:var(--red);line-height:1;transform-origin:left top}
.reach-copy{left:190px;top:221px;font-family:"Josefin Sans",sans-serif;font-weight:600;font-size:19px;line-height:21px;transform:scaleX(.8);transform-origin:left top}
.reach-copy .blue{color:var(--blue)}
.maps-row{left:190px;top:283px;width:150px;height:13px;background:var(--red);border-radius:3px}
.people{height:36px;border-radius:4px}
.caption{font-size:9px;font-stretch:100%}

/* shop locally */
.shop-line{font-family:"Josefin Sans",sans-serif;font-weight:400;line-height:1;left:438px}
.shop-ref{font-family:"Josefin Sans",sans-serif;font-size:14px;left:589px;top:366px}
.shop-chart{left:626px;top:224px;width:2px;height:192px;background:var(--ink)}
.sbar{left:628px;height:14px;background:var(--red);font-family:"Oswald",sans-serif;font-size:8.5px;color:#fff;text-align:right;padding-right:4px;line-height:14px;text-transform:uppercase}
.sbar b{position:absolute;left:100%;padding-left:3px;color:var(--ink);font-weight:400;font-size:10px}

/* ten reasons */
.ten{left:36px;top:456px;font-size:180px;color:var(--blue);transform:scaleX(.72)}
.reasons{left:162px;top:458px;font-size:76px;letter-spacing:1px}
.reasons-sub{left:162px;font-family:"Oswald",sans-serif;font-weight:300;font-size:30px;color:var(--grey);line-height:1}

/* reason blocks */
.icon{width:66px;height:66px}
.head{font-family:"Oswald",sans-serif;font-weight:400;color:var(--red);font-size:28px;line-height:1}
.body{font-size:11px;line-height:1.45;font-weight:600;white-space:normal}
.ebar{left:233px;height:19px;background:var(--red);color:#fff;font-family:"Oswald",sans-serif;font-size:10px;text-transform:uppercase;text-align:right;padding:0 5px;line-height:19px}
.ebar b{position:absolute;left:100%;padding-left:3px;color:var(--ink);font-weight:400;font-size:13px}
.medium{left:200px;width:26px;height:19px;background:var(--mid-grey);border-radius:2px}
.map-stat{display:flex;align-items:center;justify-content:center;color:#fff;font-family:"Oswald",sans-serif;font-weight:500;font-size:42px;border-radius:22px 30px 18px 40px}
.vline{width:2px;background:var(--ink)}
.lead{font-family:"Oswald",sans-serif;color:var(--blue);font-size:12px;line-height:1.3;text-transform:uppercase;white-space:normal}
.copy{font-size:11.5px;line-height:18px;font-weight:500;white-space:normal;text-align:justify}
.rbar{left:521px;height:17px;background:var(--red-soft);color:#fff;font-family:"Oswald",sans-serif;font-weight:300;font-size:9.5px;text-align:right;padding-right:5px;line-height:17px}
.rbar b{position:absolute;left:100%;padding-left:4px;color:var(--ink);font-weight:400;font-size:12px}
.not{font-family:"Bebas Neue",sans-serif;color:var(--ink);font-size:40px;vertical-align:-3px}
</style>
</head>
<body>
<main class="kit">

  <header>
    <h1>
      <span class="abs display masthead-top">AUSTRALIAN</span>
      <span class="abs display masthead-main">COMMUNITY NEWSPAPERS</span>
    </h1>
    <p class="abs bubble">Create traffic, move merchandise,<br>and establish brands in today's<br>fast-paced society</p>
  </header>
  <div class="abs hatch" style="top:194px"></div>

  <section>
    <div class="abs big-stat" style="left:36px;top:194px;font-size:108px;transform:scaleX(.6)">4.8M</div>
    <p class="abs reach-copy">AUSTRALIANS<br><span class="blue">READ A LOCAL PAPER<br>EACH WEEK [5]</span></p>
    <div class="abs maps-row" role="img" aria-label="Row of small maps of Australia"></div>
    <div class="abs rule" style="left:24px;top:308px;width:395px"></div>

    <div class="abs big-stat" style="left:36px;top:315px;font-size:52px">85%</div>
    <div class="abs people" style="left:149px;top:322px;width:212px;background:var(--red)" role="img" aria-label="Row of ten people figures, 85% highlighted red"></div>
    <div class="abs people" style="left:364px;top:322px;width:17px;background:#9a8e8e"></div>
    <p class="abs caption" style="left:150px;top:361px">believe their local community is important to them [5]</p>

    <div class="abs big-stat" style="left:36px;top:369px;font-size:52px;color:var(--blue)">89%</div>
    <div class="abs people" style="left:149px;top:377px;width:216px;background:var(--blue)" role="img" aria-label="Row of ten people figures, 89% highlighted blue"></div>
    <div class="abs people" style="left:368px;top:377px;width:13px;background:var(--mid-grey)"></div>
    <p class="abs caption" style="left:150px;top:417px">like to know what's going on in their local community [5]</p>
  </section>

  <section>
    <h2>
      <span class="abs shop-line" style="top:227px;font-size:52px">LOCAL</span>
      <span class="abs shop-line" style="top:274px;font-size:52px">PAPER</span>
      <span class="abs shop-line" style="top:319px;font-size:38px">READERS</span>
      <span class="abs shop-line" style="top:349px;font-size:38px">SHOP</span>
      <span class="abs shop-ref">[2]</span>
      <span class="abs shop-line" style="top:380px;font-size:38px">LOCALLY</span>
    </h2>
    <div class="abs shop-chart"></div>
    <div class="abs sbar" style="top:226px;width:88px"><b>41%</b></div>
    <div class="abs sbar" style="top:242px;width:110px">Professional services<b>44%</b></div>
    <div class="abs sbar" style="top:258px;width:110px"><b>44%</b></div>
    <div class="abs sbar" style="top:274px;width:112px">Home entertainment<b>45%</b></div>
    <div class="abs sbar" style="top:290px;width:120px"><b>48%</b></div>
    <div class="abs sbar" style="top:306px;width:142px">Hardware<b>61%</b></div>
    <div class="abs sbar" style="top:322px;width:145px"><b>62%</b></div>
    <div class="abs sbar" style="top:338px;width:150px">Hair &amp; beauty<b>65%</b></div>
    <div class="abs sbar" style="top:354px;width:155px"><b>68%</b></div>
    <div class="abs sbar" style="top:370px;width:160px">Takeaway food/ restaurants<b>70%</b></div>
    <div class="abs sbar" style="top:386px;width:168px"><b>75%</b></div>
    <div class="abs sbar" style="top:402px;width:183px">Groceries<b>85%</b></div>
  </section>
  <div class="abs hatch" style="top:435px"></div>

  <h2>
    <span class="abs display ten">10</span>
    <span class="abs display reasons">REASONS</span>
    <span class="abs reasons-sub" style="top:527px;letter-spacing:3px">TO ADVERTISE IN</span>
    <span class="abs reasons-sub" style="top:559px;letter-spacing:1px">YOUR LOCAL PAPER</span>
  </h2>

  <!-- left column -->
  <article>
    <svg class="abs icon" style="left:25px;top:625px" viewBox="0 0 66 66"><circle cx="35" cy="35" r="30" fill="var(--red-soft)"/><circle cx="31" cy="31" r="30" fill="var(--blue)"/><path d="M20 32h7v14h-7zM29 46V30l7-11c3 0 4 2 3 6l-2 5h10c3 0 4 3 3 5l-3 9c-1 2-2 2-4 2z" fill="#fff"/></svg>
    <h3 class="abs head" style="left:94px;top:627px">Effective</h3>
    <p class="abs" style="left:96px;top:667px;width:90px;white-space:normal;font-family:'Oswald',sans-serif;color:var(--blue);font-size:13px;font-weight:300;line-height:17.4px">I have visited a store/business because of advertising in this source. [2]</p>
    <div class="abs medium" style="top:634px"></div>
    <div class="abs medium" style="top:665px"></div>
    <div class="abs medium" style="top:694px"></div>
    <div class="abs medium" style="top:722px"></div>
    <div class="abs ebar" style="top:634px;width:174px">Local paper<b>62%</b></div>
    <div class="abs ebar" style="top:665px;width:112px">Letterboxed material<b>35%</b></div>
    <div class="abs ebar" style="top:694px;width:56px">Local TV<b>17%</b></div>
    <div class="abs ebar" style="top:722px;width:64px">Local radio<b>16%</b></div>
  </article>
  <div class="abs rule" style="left:24px;top:754px;width:395px"></div>

  <article>
    <svg class="abs icon" style="left:25px;top:765px" viewBox="0 0 66 66"><circle cx="35" cy="35" r="30" fill="var(--red-soft)"/><circle cx="31" cy="31" r="30" fill="var(--blue)"/><circle cx="31" cy="31" r="17" fill="none" stroke="#fff" stroke-width="4"/><path d="M15 30h32M31 31v16" stroke="#fff" stroke-width="4"/></svg>
    <h3 class="abs head" style="left:97px;top:767px">Drives readers to your website</h3>
    <div class="abs map-stat" style="left:97px;top:806px;width:103px;height:84px;background:var(--red)" role="img" aria-label="Map of Australia in red">44%</div>
    <div class="abs vline" style="left:212px;top:807px;height:45px"></div>
    <p class="abs lead" style="left:224px;top:810px;width:180px">Of Australian adults went to a site after seeing a local paper ad</p>
    <p class="abs copy" style="left:224px;top:848px;width:178px">Print and the internet work very well together. Print is the "push" that complements the web's "pull."</p>
  </article>
  <div class="abs rule" style="left:24px;top:928px;width:395px"></div>

  <article>
    <svg class="abs icon" style="left:25px;top:935px" viewBox="0 0 66 66"><circle cx="35" cy="35" r="30" fill="var(--red-soft)"/><circle cx="31" cy="31" r="30" fill="var(--blue)"/><circle cx="31" cy="27" r="8" fill="#fff"/><path d="M19 46c2-8 22-8 24 0z" fill="#fff"/></svg>
    <h3 class="abs head" style="left:92px;top:938px">Builds awareness of your brand</h3>
    <div class="abs map-stat" style="left:92px;top:980px;width:101px;height:94px;background:var(--blue)" role="img" aria-label="Map of Australia in blue">63%</div>
    <div class="abs vline" style="left:202px;top:980px;height:34px"></div>
    <p class="abs lead" style="left:215px;top:982px;width:190px">Of readers keep their localpaper until the next issue arrives [4]</p>
    <p class="abs copy" style="left:215px;top:1019px;width:200px">This means your ad can be in front of readers all year long, building brand awareness. When a reader needs your product or service, they will think of you first.</p>
  </article>
  <div class="abs rule" style="left:24px;top:1096px;width:395px"></div>

  <article>
    <svg class="abs icon" style="left:25px;top:1104px" viewBox="0 0 66 66"><circle cx="35" cy="35" r="30" fill="var(--red-soft)"/><circle cx="31" cy="31" r="30" fill="var(--blue)"/><circle cx="31" cy="31" r="17" fill="none" stroke="#fff" stroke-width="4"/></svg>
    <h3 class="abs head" style="left:99px;top:1110px">Brand credibility</h3>
    <p class="abs" style="left:99px;top:1146px;font-size:10.5px;line-height:17px;font-weight:500">Consumers trust their local paper more than any other media.[2]<br>The newspaper editorial environment adds instant credibility to your brand.</p>
  </article>

  <!-- right column -->
  <article>
    <svg class="abs icon" style="left:440px;top:449px" viewBox="0 0 66 66"><circle cx="35" cy="35" r="30" fill="var(--red-soft)"/><circle cx="31" cy="31" r="30" fill="var(--blue)"/><circle cx="31" cy="26" r="11" fill="none" stroke="#fff" stroke-width="3"/><rect x="26" y="38" width="10" height="8" fill="#fff"/></svg>
    <h3 class="abs head" style="left:513px;top:450px">Affordable</h3>
    <p class="abs body" style="left:513px;top:484px;width:326px">From just $20 per day, a sustained local paper ad campaign reaches more prospects at a lothan all other media advertising.</p>
  </article>
  <div class="abs rule" style="left:438px;top:528px;width:405px"></div>

  <article>
    <svg class="abs icon" style="left:440px;top:534px" viewBox="0 0 66 66"><circle cx="35" cy="35" r="30" fill="var(--red-soft)"/><circle cx="31" cy="31" r="30" fill="var(--blue)"/><g fill="none" stroke="#fff" stroke-width="3"><path d="M22 24a12 12 0 0 1 18 0M17 19a19 19 0 0 1 28 0"/></g><circle cx="31" cy="31" r="4" fill="#fff"/><path d="M31 33v14" stroke="#fff" stroke-width="3"/></svg>
    <h3 class="abs head" style="left:513px;top:535px">Highly targeted</h3>
    <p class="abs body" style="left:513px;top:566px;width:326px">Easily target your desired demographic by placing your ad in the appropriate section of the paper (entertainment, seniors, sports etc)</p>
  </article>
  <div class="abs rule" style="left:438px;top:608px;width:405px"></div>

  <article>
    <svg class="abs icon" style="left:440px;top:619px" viewBox="0 0 66 66"><circle cx="35" cy="35" r="30" fill="var(--red-soft)"/><circle cx="31" cy="31" r="30" fill="var(--blue)"/><g fill="none" stroke="#fff" stroke-width="3"><path d="M18 25v-7h7M18 18l8 8M44 25v-7h-7M44 18l-8 8M18 37v7h7M18 44l8-8M44 37v7h-7M44 44l-8-8"/></g></svg>
    <h3 class="abs head" style="left:513px;top:625px">Size does <span class="not">NOT</span> matter</h3>
    <p class="abs" style="left:513px;top:661px;font-size:10.5px;line-height:17px;font-weight:500">An ad as small as 1/8 of a page can be just as effective as a large ad. [3]<br>More important is the offer, the copy and the creative aspect of the ad.</p>
  </article>
  <div class="abs rule" style="left:438px;top:702px;width:405px"></div>

  <article>
    <svg class="abs icon" style="left:440px;top:708px" viewBox="0 0 66 66"><circle cx="35" cy="35" r="30" fill="var(--red-soft)"/><circle cx="31" cy="31" r="30" fill="var(--blue)"/><path d="M31 31L31 16M31 31L19 41M31 31L44 38" stroke="#fff" stroke-width="3"/><circle cx="31" cy="31" r="5" fill="#fff"/><circle cx="31" cy="15" r="4" fill="#fff"/><circle cx="18" cy="42" r="4" fill="#fff"/><circle cx="45" cy="39" r="4" fill="#fff"/></svg>
    <h3 class="abs head" style="left:513px;top:716px">Instant reach</h3>
    <p class="abs body" style="left:513px;top:749px;width:326px">The door-to-door home delivery model of local papers means your ad is seen by your entire local market, within days of placing your ad.</p>
  </article>
  <div class="abs rule" style="left:438px;top:796px;width:405px"></div>

  <article>
    <svg class="abs icon" style="left:440px;top:812px" viewBox="0 0 66 66"><circle cx="35" cy="35" r="30" fill="var(--red-soft)"/><circle cx="31" cy="31" r="30" fill="var(--blue)"/><path d="M12 28h38M16 28c0 8 4 10 8 10s6-4 6-10M32 28c0 8 3 10 7 10s8-2 8-10" fill="#fff" stroke="#fff" stroke-width="2"/></svg>
    <h3 class="abs head" style="left:513px;top:810px;line-height:33px">Audiences pay attention to<br>your ad</h3>
    <p class="abs body" style="left:513px;top:875px;width:330px;font-size:9.5px;line-height:1.4;font-weight:400">8 in 10 local paper readers actively look at the ads when reading the paper.[1]<br>Unlike other forms of advertising, local paper advertising is not an annoyance for consumers. To the readers, the ads are as important as the news.</p>
  </article>
  <div class="abs rule" style="left:438px;top:928px;width:405px"></div>

  <article>
    <svg class="abs icon" style="left:440px;top:939px" viewBox="0 0 66 66"><circle cx="35" cy="35" r="30" fill="var(--red-soft)"/><circle cx="31" cy="31" r="30" fill="var(--blue)"/><path d="M20 15h16l6 6v25H20z" fill="none" stroke="#fff" stroke-width="3"/><path d="M25 33l5 5 10-12" fill="none" stroke="#fff" stroke-width="3"/></svg>
    <h3 class="abs head" style="left:511px;top:941px">Results</h3>
    <p class="abs body" style="left:592px;top:940px;width:244px;font-size:11.5px;font-weight:400;line-height:1.4">In 2013, as a result of seeing an ad in a local paper, readers.[2]:</p>
    <div class="abs vline" style="left:516px;top:982px;height:196px;width:1.5px"></div>
    <div class="abs rbar" style="top:986px;width:280px">attended a local event or activity<b>84%</b></div>
    <div class="abs rbar" style="top:1010px;width:181px">talked about an ad with friends/family<b>49%</b></div>
    <div class="abs rbar" style="top:1035px;width:108px">tried a new brand<b>33%</b></div>
    <div class="abs rbar" style="top:1059px;width:169px">used a coupon/money-off voucher<b>51%</b></div>
    <div class="abs rbar" style="top:1084px;width:181px">enquired about a product/service<b>54%</b></div>
    <div class="abs rbar" style="top:1108px;width:122px">purchased a product service<b>45%</b></div>
    <div class="abs rbar" style="top:1133px;width:176px">visited a store or showroom<b>53%</b></div>
    <div class="abs rbar" style="top:1157px;width:280px">took some type of action<b>77%</b></div>
  </article>

</main>
</body>
</html>
```